Wren's Hearth Support Business Card

Business card design
Font must be in Poppins Regular for Wren's Hearth Support
Safe Days Ahead font is Alex Brush

Colour must be Hex #910E2B
RGB 145-14-43
Pantone 7427 C
We want the card editable
On the front please include
Name eg Mavis Dunleavy
Position eg Clinical Care Manager
Phone number mobile 0473 856 342
Phone 08 7394 2650
Email : mavis@wrenshearthsupport.com.au
Address : Gullwing Cove, Tidewater Shire, 6288
Website : wrenshearthsupport.com.au
Contact us today to experience the warmth, respect and personal touch of Wren's Hearth Support.

Target Market(s)

35+

Industry/Entity Type

aged care / community

Contact Information for Business Card

see project description

Requirements
Must have
• Colours, logos and fonts as detailed and uploaded

```html
<!DOCTYPE html>
<html lang="en">
<head>
<meta charset="utf-8">
<title>Wren's Hearth Support – Business Card</title>
<link href="https://fonts.googleapis.com/css2?family=Alex+Brush&family=Montserrat:ital,wght@0,400;0,500;0,700;1,700&family=Poppins:wght@400&display=swap" rel="stylesheet">
<style>
  :root {
    --brand: #910E2B;
    --ink: #1c1c1c;
    --paper: #ffffff;
    --backdrop: #ededed;
  }
  * { margin: 0; padding: 0; box-sizing: border-box; }
  html, body { width: 1200px; height: 1200px; overflow: hidden; }
  body { background: var(--backdrop); position: relative; font-family: 'Montserrat', sans-serif; }

  .card {
    position: absolute;
    left: 150px;
    width: 898px;
    height: 525px;
    background: var(--paper);
    overflow: hidden;
  }
  .card--front { top: 55px; }
  .card--back { top: 621px; }

  .front-arc { position: absolute; inset: 0; }

  .holder-name {
    position: absolute; left: 64px; top: 98px;
    font-weight: 700; font-size: 35px; letter-spacing: 0.3px;
    color: var(--brand); text-transform: uppercase;
  }
  .holder-role {
    position: absolute; left: 64px; top: 146px;
    font-size: 24px; color: var(--ink);
  }

  .contact-list { position: absolute; left: 52px; top: 274px; list-style: none; }
  .contact-item {
    display: flex; align-items: center; height: 34.5px;
    font-size: 24.5px; color: var(--ink); white-space: nowrap;
  }
  .contact-icon { width: 18px; height: 18px; margin-right: 22px; fill: var(--brand); flex: none; }
  .contact-item--web { margin-top: 20px; font-size: 22px; font-weight: 700; font-style: italic; color: var(--brand); }

  .brand-lockup {
    position: absolute; left: 220px; top: 184px;
    display: flex; align-items: center;
  }
  .brand-circle {
    width: 146px; height: 146px; border-radius: 50%;
    border: 10px solid var(--brand); flex: none; margin-right: 20px;
  }
  .brand-text { display: flex; flex-direction: column; }
  .brand-name {
    font-family: 'Poppins', sans-serif; font-weight: 400;
    font-size: 46px; line-height: 1.05; color: var(--brand);
  }
  .brand-tagline {
    font-family: 'Alex Brush', cursive;
    font-size: 42px; line-height: 1.1; color: var(--brand); margin-top: 2px;
  }
</style>
</head>
<body>
  <section class="card card--front" aria-label="Business card front">
    <svg class="front-arc" width="898" height="525" viewBox="0 0 898 525" aria-hidden="true">
      <circle cx="216" cy="263" r="469" fill="none" stroke="var(--brand)" stroke-width="56"/>
      <rect class="arc-gap" x="600" y="148" width="200" height="228" fill="var(--paper)"/>
    </svg>

    <h1 class="holder-name">Mavis Dunleavy</h1>
    <p class="holder-role">Position eg Clinical Care Manager</p>

    <ul class="contact-list">
      <li class="contact-item">
        <svg class="contact-icon" viewBox="0 0 24 24"><path d="M7 1h10a2 2 0 0 1 2 2v18a2 2 0 0 1-2 2H7a2 2 0 0 1-2-2V3a2 2 0 0 1 2-2zm0 3v14h10V4H7zm5 15.5a1.2 1.2 0 1 0 0 2.4 1.2 1.2 0 0 0 0-2.4z"/></svg>
        0473 856 342
      </li>
      <li class="contact-item">
        <svg class="contact-icon" viewBox="0 0 24 24"><path d="M6.6 10.8a15.2 15.2 0 0 0 6.6 6.6l2.2-2.2a1 1 0 0 1 1-.25 11.4 11.4 0 0 0 3.6.57 1 1 0 0 1 1 1V20a1 1 0 0 1-1 1A17 17 0 0 1 3 4a1 1 0 0 1 1-1h3.5a1 1 0 0 1 1 1c0 1.25.2 2.45.57 3.57a1 1 0 0 1-.25 1l-2.2 2.2z"/></svg>
        08 7394 2650
      </li>
      <li class="contact-item">
        <svg class="contact-icon" viewBox="0 0 24 24"><path d="M3 5h18a1 1 0 0 1 1 1v12a1 1 0 0 1-1 1H3a1 1 0 0 1-1-1V6a1 1 0 0 1 1-1zm9 7.5L4 7.6V9l8 4.9L20 9V7.6l-8 4.9z"/></svg>
        mavis@wrenshearthsupport.com.au
      </li>
      <li class="contact-item">
        <svg class="contact-icon" viewBox="0 0 24 24"><path d="M12 1a8 8 0 0 0-8 8c0 6 8 14 8 14s8-8 8-14a8 8 0 0 0-8-8zm0 11a3 3 0 1 1 0-6 3 3 0 0 1 0 6z"/></svg>
        Gullwing Cove, Tidewater Shire, 6288
      </li>
      <li class="contact-item contact-item--web">
        <svg class="contact-icon" viewBox="0 0 24 24"><path d="M12 2a10 10 0 1 0 0 20 10 10 0 0 0 0-20zm6.9 6h-3a15 15 0 0 0-1.3-3.9A8 8 0 0 1 18.9 8zM12 4c.8 1.1 1.5 2.5 1.9 4h-3.8c.4-1.5 1.1-2.9 1.9-4zM4.3 14a8 8 0 0 1 0-4h3.4a16 16 0 0 0 0 4H4.3zm.8 2h3a15 15 0 0 0 1.3 3.9A8 8 0 0 1 5.1 16zm3-8h-3a8 8 0 0 1 4.3-3.9A15 15 0 0 0 8.1 8zM12 20c-.8-1.1-1.5-2.5-1.9-4h3.8c-.4 1.5-1.1 2.9-1.9 4zm2.3-6H9.7a14 14 0 0 1 0-4h4.6a14 14 0 0 1 0 4zm.3 5.9a15 15 0 0 0 1.3-3.9h3a8 8 0 0 1-4.3 3.9zM16.3 14a16 16 0 0 0 0-4h3.4a8 8 0 0 1 0 4h-3.4z"/></svg>
        wrenshearthsupport.com.au
      </li>
    </ul>
  </section>

  <section class="card card--back" aria-label="Business card back">
    <div class="brand-lockup">
      <div class="brand-circle" aria-hidden="true"></div>
      <div class="brand-text">
        <span class="brand-name">Wren's Hearth<br>Support</span>
        <span class="brand-tagline">Safe Days Ahead</span>
      </div>
    </div>
  </section>
</body>
</html>
```